Business Card with Logo and Company Name.

I would like a business card design that has both my logo and company name. The K7 logo was one part- now I would like the entire Company Name.

KESTRO CONTRACTING SERVICES

I have consulted with my team and we have went over several ideas for the last few weeks. We all love the K7 logo. Great for branding. What we have thought of in regards to the company name to tie into it is giving focus to font selection. We love the idea of KESTRO being a larger font and maybe making CONTRACTING SERVICES a larger font. Much like one would for a Slogan Line and font when designing.

I hope I’m communicating this correctly and not causing confusion. If need be I can mock up or sketch an idea and send. Just let me know.

**** I just noticed an area to upload an image. I uploaded one that was used as an idea*****

```html
<!DOCTYPE html>
<html lang="en">
<head>
<meta charset="utf-8">
<title>Kestro Contracting Services – Business Card</title>
<link rel="stylesheet" href="https://fonts.googleapis.com/css2?family=Cinzel:wght@400&family=Montserrat:wght@400;500;700&display=swap">
<style>
  :root {
    --brand-red: #e63c41;
    --card-white: #f4f4f4;
    --ink-grey: #5d5d60;
    --page-bg: #c9c7c6;
    --text-white: #ffffff;
  }
  * { margin: 0; padding: 0; box-sizing: border-box; }
  html, body { width: 1200px; height: 1200px; overflow: hidden; }
  body { background: var(--page-bg); position: relative; font-family: "Montserrat", sans-serif; }

  .card {
    position: absolute;
    left: 243px;
    width: 702px;
    height: 400px;
    border-radius: 22px;
    overflow: hidden;
  }
  .card--front { top: 170px; background: var(--brand-red); color: var(--text-white); }
  .card--back { top: 630px; background: var(--card-white); }

  .brand-mark {
    position: absolute;
    border-radius: 50%;
  }
  .card--front .brand-mark { left: 291px; top: 76px; width: 120px; height: 120px; background: var(--text-white); }
  .card--back .brand-mark { left: 152px; top: 106px; width: 100px; height: 100px; background: var(--brand-red); }

  .wordmark {
    position: absolute;
    left: 0; right: 0;
    text-align: center;
    font-family: "Cinzel", serif;
    font-weight: 400;
    line-height: 1;
    white-space: nowrap;
  }
  .card--front .wordmark__name { top: 228px; font-size: 58px; letter-spacing: 2px; }
  .card--front .wordmark__tagline { top: 286px; font-size: 16px; letter-spacing: 1px; }
  .established {
    position: absolute;
    left: 0; right: 0; top: 368px;
    text-align: center;
    font-family: "Cinzel", serif;
    font-size: 14px;
    letter-spacing: 3px;
    line-height: 1;
  }

  .card--back .wordmark { left: 80px; right: auto; width: 244px; color: var(--brand-red); }
  .card--back .wordmark__name { top: 233px; font-size: 46px; letter-spacing: 1px; }
  .card--back .wordmark__tagline { top: 276px; font-size: 12px; letter-spacing: 0.5px; }

  .contact { position: absolute; left: 351px; top: 88px; color: var(--ink-grey); }
  .contact__name { font-weight: 700; font-size: 23px; color: var(--brand-red); letter-spacing: 0.5px; line-height: 1.1; }
  .contact__role { font-size: 16px; letter-spacing: 5px; line-height: 1.2; margin-top: 2px; }
  .contact__rule { width: 38px; height: 3px; background: var(--brand-red); margin: 10px 0 14px; }
  .contact__address { font-size: 19px; line-height: 23px; letter-spacing: 0.6px; margin-bottom: 14px; }
  .contact__line { display: flex; align-items: center; gap: 6px; font-size: 16.5px; line-height: 28px; letter-spacing: 0.4px; }
  .contact__icon { width: 17px; height: 17px; fill: var(--brand-red); flex: none; }
</style>
</head>
<body>
  <section class="card card--front" aria-label="Card front">
    <div class="brand-mark" role="img" aria-label="Company logo placeholder"></div>
    <div class="wordmark wordmark__name">KESTRO</div>
    <div class="wordmark wordmark__tagline">CONTRACTING SERVICES</div>
    <div class="established">EST.1981</div>
  </section>

  <section class="card card--back" aria-label="Card back">
    <div class="brand-mark" role="img" aria-label="Company logo placeholder"></div>
    <div class="wordmark wordmark__name">KESTRO</div>
    <div class="wordmark wordmark__tagline">CONTRACTING SERVICES</div>

    <div class="contact">
      <div class="contact__name">DANA WHITFIELD</div>
      <div class="contact__role">OWNER</div>
      <div class="contact__rule"></div>
      <div class="contact__address">82 Alder Court<br>Brookhaven, IL 60412</div>
      <div class="contact__line">
        <svg class="contact__icon" viewBox="0 0 24 24" aria-hidden="true"><path d="M6.6 10.8a15.1 15.1 0 0 0 6.6 6.6l2.2-2.2a1 1 0 0 1 1-.25 11.4 11.4 0 0 0 3.6.57 1 1 0 0 1 1 1V20a1 1 0 0 1-1 1A17 17 0 0 1 3 4a1 1 0 0 1 1-1h3.5a1 1 0 0 1 1 1c0 1.25.2 2.45.57 3.57a1 1 0 0 1-.25 1z"/></svg>
        <span>(312) 555-0147</span>
      </div>
      <div class="contact__line">
        <svg class="contact__icon" viewBox="0 0 24 24" aria-hidden="true"><path d="M2 9c0-2 4.5-4 10-4s10 2 10 4v1.5a1 1 0 0 1-1 1h-3a1 1 0 0 1-1-1V9.5c-1.5-.5-3.2-.8-5-.8s-3.5.3-5 .8v1a1 1 0 0 1-1 1H3a1 1 0 0 1-1-1z"/><path d="M7 12h10l3 7H4z M12 13.5a2.5 2.5 0 1 0 0 5 2.5 2.5 0 0 0 0-5z" fill-rule="evenodd"/></svg>
        <span>(312) 555-0182</span>
      </div>
      <div class="contact__line">
        <svg class="contact__icon" viewBox="0 0 24 24" aria-hidden="true"><path fill-rule="evenodd" d="M12 2a10 10 0 1 0 0 20 10 10 0 0 0 0-20zm-1 2.1C9.6 5.6 8.7 7.9 8.5 11h2.5zm2 0V11h2.5c-.2-3.1-1.1-5.4-2.5-6.9zM6.5 11c.1-2.5.8-4.6 1.8-6.1A8 8 0 0 0 4.1 11zm11 0h2.4a8 8 0 0 0-4.2-6.1c1 1.5 1.7 3.6 1.8 6.1zM4.1 13a8 8 0 0 0 4.2 6.1c-1-1.5-1.7-3.6-1.8-6.1zm4.4 0c.2 3.1 1.1 5.4 2.5 6.9V13zm4.5 0v6.9c1.4-1.5 2.3-3.8 2.5-6.9zm4.5 0c-.1 2.5-.8 4.6-1.8 6.1a8 8 0 0 0 4.2-6.1z"/></svg>
        <span>www.kestrocontracting.com</span>
      </div>
    </div>
  </section>
</body>
</html>
```